Create modern and sleek business card for luxury real estate company

We're a "boutique" real estate office looking for a design that gets across a highly modern luxury brand. Blacks and whites are probably the best colors unless we try a silver foil for the logo. I've attached a version of our current logo here. I'd like to swap out the current font on there with Gotham Light Regular.

I'm looking to have one side of the card have the logo with the space for our agents info on the other side.

Target Market(s)

Young professionals in a "luxury" headspace

Industry/Entity Type

Real estate

Contact Information for Business Card

A place for agent name, cell number, website. The slogan "Living Well, Moving Forward".

Font styles to use
Other font styles liked:
• Gotham Regular

Colors

Designer to choose only greyscale colors for use in the design.

Requirements
Must have
• Matte black as the background color. Clean lines and use of contrast. A specific design aspect that will use silver foil.
Nice to have
• Up in the air on integrating a QR code
Should not have
• Any houses or other real estate related design (ex: a clip art house)

```html
<!DOCTYPE html>
<html lang="en">
<head>
<meta charset="utf-8">
<title>Halvor Realty – Business Card</title>
<link rel="stylesheet" href="https://fonts.googleapis.com/css2?family=Montserrat:wght@300;400;600&family=Arimo:wght@400&display=swap">
<style>
  :root {
    --stage: #2a2a2a;
    --matte-black: #232325;
    --silver: #e9e9ea;
    --paper: #ffffff;
    --ink: #1e1e1e;
    --ink-soft: #8c8c8c;
    --band: #3a3a3c;
    --band-light: #bdbdbd;
  }
  html, body {
    margin: 0;
    padding: 0;
    width: 1200px;
    height: 900px;
    overflow: hidden;
    background: var(--stage);
  }
  .canvas {
    position: relative;
    width: 1200px;
    height: 900px;
  }
  .card {
    position: absolute;
    width: 640px;
    height: 366px;
    box-shadow: 0 18px 40px rgba(0,0,0,0.55);
    overflow: hidden;
  }

  /* Shared company name */
  .company-name {
    position: absolute;
    margin: 0;
    font-family: "Montserrat", sans-serif;
    font-weight: 400;
    letter-spacing: 0.08em;
    text-transform: uppercase;
    line-height: 1;
    white-space: nowrap;
  }

  /* Front side */
  .card--front {
    left: 190px;
    top: 60px;
    background: var(--matte-black);
  }
  .card--front .company-name {
    left: 0;
    right: 0;
    top: 160px;
    text-align: center;
    font-size: 44px;
    color: var(--silver);
  }

  /* Back side */
  .card--back {
    left: 370px;
    top: 480px;
    background: var(--paper);
  }
  .card--back .company-name {
    left: 40px;
    top: 44px;
    font-size: 26px;
    color: var(--ink);
  }
  .agent {
    position: absolute;
    right: 34px;
    top: 30px;
    text-align: right;
    font-family: "Montserrat", sans-serif;
  }
  .agent__name {
    font-size: 22px;
    font-weight: 600;
    color: #3b3b3b;
  }
  .agent__role {
    font-size: 13px;
    font-weight: 400;
    color: var(--ink-soft);
  }
  .contact {
    position: absolute;
    left: 40px;
    top: 150px;
    margin: 0;
    padding: 0;
    list-style: none;
    font-family: "Arimo", sans-serif;
    font-size: 15px;
    color: var(--ink);
  }
  .contact__item {
    display: flex;
    align-items: center;
    gap: 16px;
    line-height: 19px;
  }
  .contact__item--address {
    margin-bottom: 16px;
  }
  .contact__icon {
    width: 14px;
    height: 14px;
    flex: none;
    fill: #444;
  }
  .footer-band {
    position: absolute;
    left: 0;
    bottom: 0;
    width: 640px;
    height: 58px;
  }
  .slogan {
    position: absolute;
    left: 40px;
    bottom: 10px;
    font-family: "Montserrat", sans-serif;
    font-weight: 300;
    font-size: 17px;
    letter-spacing: 0.06em;
    text-transform: uppercase;
    color: #f2f2f2;
    margin: 0;
  }
</style>
</head>
<body>
<main class="canvas">

  <section class="card card--front" aria-label="Card front">
    <p class="company-name">Halvor Realty</p>
  </section>

  <section class="card card--back" aria-label="Card back">
    <p class="company-name">Halvor Realty</p>

    <div class="agent">
      <div class="agent__name">Marco Velden</div>
      <div class="agent__role">Agent</div>
    </div>

    <ul class="contact">
      <li class="contact__item contact__item--address">
        <svg class="contact__icon" viewBox="0 0 14 14"><path d="M7 0a4.5 4.5 0 0 0-4.5 4.5C2.5 8 7 14 7 14s4.5-6 4.5-9.5A4.5 4.5 0 0 0 7 0zm0 6.3a1.8 1.8 0 1 1 0-3.6 1.8 1.8 0 0 1 0 3.6z"/></svg>
        <span>48 Alder Lane<br>Westbrook MA 02190</span>
      </li>
      <li class="contact__item">
        <svg class="contact__icon" viewBox="0 0 14 14"><path d="M3 0l2 3-1.3 1.6a8 8 0 0 0 5.7 5.7L11 9l3 2-1 2.5C6 14 0 8 0.5 1z"/></svg>
        <span>555 240 1100</span>
      </li>
      <li class="contact__item">
        <svg class="contact__icon" viewBox="0 0 14 14"><path d="M3 0h8v4H3zM1 5h12v6h-2v3H3v-3H1zm3 4v4h6V9z"/></svg>
        <span>555 240 1101</span>
      </li>
      <li class="contact__item">
        <svg class="contact__icon" viewBox="0 0 14 14"><path d="M3.5 0h7v14h-7zM5 1.5v9.5h4V1.5zM6.3 12h1.4v1H6.3z"/></svg>
        <span>555 240 1177</span>
      </li>
      <li class="contact__item">
        <svg class="contact__icon" viewBox="0 0 14 14"><path d="M0 3h14v8H0zm1.2 1l5.8 4 5.8-4z"/></svg>
        <span>hello@halvorhomes.com</span>
      </li>
      <li class="contact__item">
        <svg class="contact__icon" viewBox="0 0 14 14"><circle cx="7" cy="7" r="6.3" fill="none" stroke="#444" stroke-width="1.2"/><path d="M0.7 7h12.6M7 0.7v12.6M7 0.7c-3 3.5-3 9 0 12.6M7 0.7c3 3.5 3 9 0 12.6" fill="none" stroke="#444" stroke-width="1"/></svg>
        <span>www.halvorhomes.com</span>
      </li>
    </ul>

    <svg class="footer-band" viewBox="0 0 640 58" aria-hidden="true">
      <polygon points="410,26 640,26 640,32 416,32" fill="var(--band-light)"/>
      <polygon points="0,14 392,14 414,40 640,40 640,58 0,58" fill="var(--band)"/>
    </svg>
    <p class="slogan">Living Well, Moving Forward</p>
  </section>

</main>
</body>
</html>
```